Professional website for psychological services

Create a professional, easy to navigate website using soothing coastal images and incorporate company logo in design. Website is for a small private clinic that provides psychological services and must be appealing to professional men and women. A website I really like is www.velmorlodge.example I would love something like similar.

Target Market(s)

Professional men and women seeking psychological services

Industry/Entity Type

Mental Health

Number of Pages Required

5+ page

Requirements
Must have
• The website must incorporate the logo provided. The name of the company/website is Brindle Oak Wellness Aftercare. Colors must compliment the logo, must be coastal and soothing yet very professional. I would like a website like www.velmorlodge.example
• Pages will be:Home, Services, FAQ and Contact Us. The images included of the building and office are for the contact us page. Under the tab Servies: Individual Psychotherapy, Family Therapy, EMDR I will provide specific content for each.
Nice to have
• I want the website to be easy to navigate and the font easy to read. The writing on the logo is very light and I'm open to changing it slightly if it will be better aesthetically.
Should not have
• Please no pictures of any swimsuits, alcoholic beverages, etc. This is a professional psychological clinic.

```html
<!DOCTYPE html>
<html lang="en">
<head>
<meta charset="utf-8">
<title>Brindle Oak Wellness Aftercare</title>
<link rel="stylesheet" href="https://fonts.googleapis.com/css2?family=Playfair+Display:wght@400;700&family=Arimo:wght@400;700&display=swap">
<style>
:root{
  --teal:#1fb3cc;
  --ink:#1d1d1d;
  --text:#2b2b2b;
  --muted:#6b6b6b;
  --panel:rgba(38,42,46,.86);
  --card:#efe9e3;
  --white:#ffffff;
}
*{margin:0;padding:0;box-sizing:border-box}
html,body{width:1200px;height:3163px;overflow:hidden;background:var(--white)}
body{position:relative;font-family:"Arimo",Arial,sans-serif;color:var(--text)}
.abs{position:absolute}

/* hero */
.hero{left:0;top:0;width:1200px;height:896px;
  background:linear-gradient(180deg,#ffffff 0,#ffffff 190px,#bfe7e6 300px,#8fd2cf 520px,#a6d9d2 760px,#cfe9e6 896px)}
.hero-land{left:560px;top:230px;width:640px;height:666px;
  background:linear-gradient(120deg,rgba(120,160,120,.35),rgba(170,190,150,.55) 60%,rgba(210,220,200,.5))}
.brand{left:0;top:50px;width:1200px;text-align:center}
.brand-dot{display:block;width:34px;height:34px;border-radius:50%;background:var(--teal);margin:0 auto 22px;opacity:.85}
.brand-name{font-family:"Playfair Display",Georgia,serif;font-weight:400;font-size:30px;color:var(--teal);letter-spacing:.5px}
.nav{left:0;top:246px;width:1200px;height:20px}
.nav a{position:absolute;top:0;transform:translateX(-50%);font-size:14px;color:var(--ink);text-decoration:none;letter-spacing:.5px;text-transform:uppercase}
.nav .sep{position:absolute;top:2px;width:1px;height:16px;background:#8aa9aa}
.hero-card{left:48px;top:468px;width:658px;height:243px;background:rgba(220,240,240,.45);border-left:9px solid var(--teal);padding:24px 0 0 26px}
.hero-title{font-family:"Playfair Display",Georgia,serif;font-size:42px;line-height:50px;color:var(--ink);font-weight:400}
.hero-quote{margin-top:22px;font-size:17px;line-height:23px;color:var(--muted);width:610px}
.social{left:66px;top:722px}
.social span{display:inline-block;width:28px;height:28px;border-radius:50%;border:2px solid #ffffff;background:rgba(255,255,255,.25);margin-right:8px}
.portrait{left:771px;top:436px;width:330px;height:330px;border-radius:50%;border:8px solid rgba(255,255,255,.9);
  background:radial-gradient(circle at 50% 40%,#c99f86 0,#7a5040 45%,#4c8f86 75%,#6fb5a6 100%)}

/* listings */
.rule{left:0;width:1200px;height:8px;background:var(--teal)}
.listings{left:0;top:904px;width:1200px;height:346px;display:flex}
.listings div{flex:1}
.l1{background:linear-gradient(180deg,#8fb4d0,#5d7f6c 70%,#2f3a33)}
.l2{background:linear-gradient(180deg,#3e6a3a,#4a4c4a 60%,#2e2f30)}
.l3{background:linear-gradient(180deg,#2d6fb0,#d9b8c4 50%,#9ec4c8)}
.l4{background:linear-gradient(180deg,#8a4a6a,#d14a55 55%,#c9b39a)}
.l5{background:linear-gradient(180deg,#e4b79c,#c67a63 55%,#5a3430)}
.listing-label{left:0;top:907px;width:415px;height:36px;background:rgba(235,240,242,.9);font-weight:700;font-size:18px;line-height:36px;color:var(--teal);padding-left:20px}

/* about / press */
.story{left:0;top:1259px;width:1200px;height:1068px;
  background:linear-gradient(180deg,#dfe9f3 0,#c9d9e6 260px,#a9b7a8 560px,#6fc6d3 760px,#3fb0c6 900px,#9fd4dc 1068px)}
.section-title{font-family:"Playfair Display",Georgia,serif;font-weight:400;color:var(--ink)}
.about-title{left:78px;top:1384px;font-size:46px}
.about-line{left:0;top:1460px;width:126px;height:5px;background:var(--teal)}
.about-text{left:78px;top:1486px;width:520px;font-size:15.5px;line-height:24px;color:var(--ink);text-align:justify}
.frame{border:3px solid var(--ink)}
.photo{box-shadow:0 6px 18px rgba(0,0,0,.25)}
.about-frame{left:797px;top:1407px;width:342px;height:344px}
.about-photo{left:666px;top:1373px;width:420px;height:323px;background:linear-gradient(160deg,#7d6a60,#b79a88 45%,#e7e2de 80%,#9a6c5a)}
.press-frame{left:78px;top:1898px;width:337px;height:342px}
.press-photo{left:124px;top:1862px;width:420px;height:323px;background:radial-gradient(circle at 30% 30%,#d7a25a 0,#5a3a22 45%,#2c2220 80%)}
.press-title{right:82px;top:1904px;font-size:44px;text-transform:uppercase;text-align:right}
.press-line{left:1030px;top:1980px;width:170px;height:5px;background:var(--teal)}
.press-text{left:610px;top:2002px;width:508px;font-size:15.5px;line-height:23px;color:var(--ink);text-align:justify;text-align-last:right}

/* contact */
.contact-bg{left:0;top:2327px;width:1200px;height:773px;
  background:linear-gradient(180deg,#ffffff 0,#ffffff 120px,#b9cfc4 260px,#6aa8a8 450px,#39a7b8 620px,#bfe2e6 773px)}
.info-panel{left:150px;top:2505px;width:529px;height:465px;background:var(--panel)}
.tag{position:absolute;left:150px;background:var(--teal);color:var(--white);font-family:"Playfair Display",Georgia,serif;font-size:26px;line-height:34px;padding-left:38px;text-transform:uppercase}
.tag-spec{top:2541px;width:308px}
.tag-addr{top:2742px;width:183px}
.tag-cont{top:2855px;width:183px}
.spec-list{left:194px;top:2585px;list-style:none;font-size:11px;font-weight:700;line-height:12.5px;color:var(--white);text-transform:uppercase}
.spec-list li::before{content:"";display:inline-block;width:6px;height:6px;border-radius:50%;background:var(--teal);margin-right:8px;vertical-align:1px}
.info-text{left:188px;font-size:11px;font-weight:700;line-height:13px;color:var(--white);text-transform:uppercase}
.connector{left:660px;top:2525px;width:40px;height:3px;background:var(--ink)}
.contact-card{left:679px;top:2453px;width:390px;height:563px;background:var(--card);box-shadow:0 4px 14px rgba(0,0,0,.2)}
.contact-title{left:713px;top:2498px;font-size:46px}
.field{left:713px;width:316px;height:31px;border:2px solid #333;font-size:10px;color:#555;padding:8px 0 0 10px}
.field b{color:var(--teal);font-weight:700}
.f-name{top:2592px}.f-mail{top:2657px}.f-phone{top:2725px}.f-msg{top:2788px;height:116px}
.submit{left:924px;top:2936px;width:105px;height:24px;background:var(--teal);color:var(--white);font-size:10px;font-weight:700;text-align:center;line-height:24px}

.footer{left:0;top:3100px;width:1200px;height:63px;text-align:center;font-size:9px;line-height:13px;color:var(--muted);padding-top:20px}
</style>
</head>
<body>

<header>
  <div class="abs hero" role="img" aria-label="Aerial view of a turquoise coastline with beach, boats and tree-lined villas"></div>
  <div class="abs hero-land" role="img" aria-label="Green hillside with houses seen from above"></div>
  <div class="abs brand"><span class="brand-dot"></span><span class="brand-name">Brindle Oak Wellness Aftercare</span></div>
  <nav class="abs nav">
    <a href="#" style="left:338px">Home</a><span class="sep" style="left:418px"></span>
    <a href="#" style="left:508px">Services</a><span class="sep" style="left:599px"></span>
    <a href="#" style="left:671px">FAQ</a><span class="sep" style="left:749px"></span>
    <a href="#" style="left:836px">Contact Us</a>
  </nav>
</header>

<section>
  <div class="abs hero-card">
    <h1 class="hero-title">Face significant life challenges<br>with grace and courage</h1>
    <p class="hero-quote">"My purpose in life is to be productive, to be trustworthy, to be compassion­ate, and to inspire the untapped potential in another."</p>
  </div>
  <div class="abs social"><span></span><span></span><span></span></div>
  <div class="abs portrait" role="img" aria-label="Portrait photo of the lead psychologist"></div>
</section>

<section>
  <div class="abs rule" style="top:896px"></div>
  <div class="abs listings">
    <div class="l1" role="img" aria-label="Camera on a tripod overlooking mountains"></div>
    <div class="l2" role="img" aria-label="Woman in a winter coat among pine branches"></div>
    <div class="l3" role="img" aria-label="Table with flowers and lanterns by the sea"></div>
    <div class="l4" role="img" aria-label="Baby in a red holiday hat"></div>
    <div class="l5" role="img" aria-label="Woman holding a warm drink under string lights"></div>
  </div>
  <div class="abs listing-label">More Treatment Listings in Ladera Ranch</div>
  <div class="abs rule" style="top:1250px"></div>
</section>

<main>
  <div class="abs story" role="img" aria-label="Cliffside bay with turquoise water under a pale sky"></div>

  <h2 class="abs section-title about-title">About Us</h2>
  <div class="abs about-line"></div>
  <p class="abs about-text">California is the land of movie stars and computer geeks. It is also a place that has some pretty serious drug problems. It seems like California has been dealing with drugs and drug addicts since before the 49's first struck gold. Every single type of illicit drug seems to be found in California. Right now, experts estimate that approximately 855,000 people regularly use drugs.</p>
  <div class="abs frame about-frame"></div>
  <div class="abs photo about-photo" role="img" aria-label="Woman in earmuffs leaning on a snowy railing"></div>

  <div class="abs frame press-frame"></div>
  <div class="abs photo press-photo" role="img" aria-label="Woman taking a photo with a camera among warm lights"></div>
  <h2 class="abs section-title press-title">In the Press</h2>
  <div class="abs press-line"></div>
  <p class="abs press-text">Detoxing from alcohol or prescription drugs can be frustrating, even dangerous without proper supervision. If you or someone you care about is ready to attain a clean and sober life, it's important to seek medical attention to ensure the most successful rehabilitation. Whether you are looking for a Relvane treatment clinic to address Detox addiction, or a detox center to help recover from alcohol or any other illegal or prescribed drug abuse, browse the listings below to find residential and outpatient treatment alternatives in Ladera Ranch.</p>
</main>

<section>
  <div class="abs contact-bg" role="img" aria-label="Rocky island lagoon with a white boat on clear blue water"></div>
  <div class="abs info-panel"></div>
  <div class="tag tag-spec">Our Specialties:</div>
  <ul class="abs spec-list">
    <li>Evaluation and Diagnostics</li>
    <li>Depression</li>
    <li>Overcoming Fear and Anxiety</li>
    <li>Couples Counselling</li>
    <li>Coping with Stress</li>
    <li>Individual Therapy</li>
    <li>Healing the Heart</li>
    <li>Chronic Pain Treatment</li>
    <li>Critical Incident Debriefing</li>
  </ul>
  <div class="tag tag-addr">Address</div>
  <p class="abs info-text" style="top:2794px">240 Harbor Bend Road<br>Port Alder, MN 55990</p>
  <div class="tag tag-cont">Contact</div>
  <p class="abs info-text" style="top:2908px">Phone: (555) 014-2638</p>

  <div class="abs connector"></div>
  <div class="abs contact-card"></div>
  <h2 class="abs section-title contact-title">CONTACT Us</h2>
  <div class="abs field f-name">Name: <b>*</b></div>
  <div class="abs field f-mail">Email: <b>*</b></div>
  <div class="abs field f-phone">Phone:</div>
  <div class="abs field f-msg">Message:</div>
  <div class="abs submit">SUBMIT</div>
</section>

<footer class="abs footer">© 2016 Harborline Psychological Clinic. Powered by Tidewell Web Services - Shoreframe<br>R 12 4410.6</footer>

</body>
</html>
```